Need Website for PR Firm

I need a website for my new business, Harbinger Press Collective, a PR, Communications and Marketing Firm. I want something classy and clean. Tailored and professional with a bit of a whimsical touch. Colors are mainly white and green. I don't like random stock photos but I would consider an image of a park with the city in the background. The name of my company is a play on Willowmere Commons in Brooklyn where I am based.

The navigation and pages I will need is a good clean landing page.
About us
Who we are
Contact

Again, I like clean white and the copy in a similar color and font as my logo.
No stock photography or clip art.
I uploaded an image of the park that I like and wld be open to using in some way
Updates

I have uploaded an image of the park that you could implemented. 

Seeing some good designs here.

With the image I uploaded, I unfortunately think the green sky is too green.
Wondering if we can make modifications to the color of the sky.
I like the last image submitted too.

Target Market(s)

Professionals and the media who are seeing how I represent myself and my agency as they hire me for the public relations council.

Industry/Entity Type

Business

Font styles to use
Serif
Other font styles liked:
• Trajan

Colors
acd036
ffffff
dbdbdb
eeeeee

Requirements
Must have
• High quality and consistent colors and font.
Should not have
• Stock photography
Clip art
colors that aren't white, the green in my font, black or gray if necessary.

```html
<!DOCTYPE html>
<html lang="en">
<head>
<meta charset="utf-8">
<title>Harbinger Press Collective</title>
<link href="https://fonts.googleapis.com/css2?family=Yanone+Kaffeesatz:wght@400;500&display=swap" rel="stylesheet">
<style>
:root{
  --green:#8aab14;
  --green-btn:#84a60f;
  --hero:#d3d978;
  --hero-deep:#c6cf63;
  --page:#f5f5f5;
  --rule:#e6e6e6;
  --band:#e2e2e2;
  --text:#6f6f6f;
  --heading:#5a5a5a;
  --muted:#9a9a9a;
  --nav:#9a9a9a;
  --circle:#a5a5a5;
  --dark-btn:#3d3d3d;
  --footer:#545454;
  --white:#ffffff;
  --input-border:#d6d6d6;
}
*{margin:0;padding:0;box-sizing:border-box}
html,body{width:1005px;height:1200px;overflow:hidden}
body{background:var(--page);font-family:Arial,Helvetica,sans-serif;font-size:10.3px;line-height:15.5px;color:var(--text);position:relative}
.display{font-family:"Yanone Kaffeesatz",sans-serif;font-weight:400}
.wrap{position:absolute;left:137px;width:731px}

.site-header{top:24px;height:89px;border-top:1px solid var(--rule);border-bottom:1px solid var(--rule)}
.brand{position:absolute;left:0;top:16px;display:flex;align-items:center;gap:10px}
.brand-mark{width:14px;height:14px;background:var(--green)}
.brand-name{font-family:"Yanone Kaffeesatz",sans-serif;font-weight:400;color:var(--green);font-size:21px;line-height:19px;letter-spacing:.5px}
.main-nav{position:absolute;right:0;top:22px;display:flex;gap:23px}
.main-nav a{font-family:"Yanone Kaffeesatz",sans-serif;font-size:16px;color:var(--nav);text-decoration:none}
.main-nav a.active{color:var(--green);font-weight:500}

.hero{top:137px;height:279px;background:linear-gradient(180deg,var(--hero) 0%,var(--hero) 72%,#dfe0c9 84%,#e4e4e4 100%);overflow:hidden}
.hero-caption{position:absolute;left:16px;top:73px;width:270px;color:var(--white)}
.hero-caption h1{font-family:"Yanone Kaffeesatz",sans-serif;font-weight:400;font-size:25px;line-height:28px;margin-bottom:4px}
.hero-caption p{font-weight:bold;font-size:10px;line-height:15.5px}
.slider-btn{position:absolute;top:225px;width:38px;height:38px;border-radius:50%;background:var(--dark-btn);display:flex;align-items:center;justify-content:center}
.slider-btn.prev{left:635px}
.slider-btn.next{left:676px}

.band{height:11px;background:var(--band)}

.welcome{top:474px}
.welcome h2{font-family:"Yanone Kaffeesatz",sans-serif;font-weight:400;font-size:22px;line-height:24px;color:var(--heading);margin-bottom:3px}
.welcome h2 span{color:var(--green)}
.welcome p{width:450px}

.features{top:589px;height:120px}
.intro{position:absolute;left:0;top:0;width:172px;height:120px;border-right:1px solid var(--rule)}
.intro h2{font-family:"Yanone Kaffeesatz",sans-serif;font-weight:400;font-size:28px;line-height:30px;color:var(--muted);margin-top:2px}
.intro p{font-style:italic;color:var(--muted);margin-top:12px;width:160px}
.btn{display:inline-block;background:var(--green-btn);color:var(--white);font-size:8.5px;font-weight:bold;line-height:20px;padding:0 6px;text-decoration:none}
.intro .btn{margin-top:14px}
.feature{position:absolute;top:0;width:168px}
.feature .num{position:absolute;left:0;top:2px;width:25px;height:25px;border-radius:50%;background:var(--circle);color:var(--white);font-size:11px;line-height:25px;text-align:center}
.feature h3{font-family:"Yanone Kaffeesatz",sans-serif;font-weight:400;font-size:17px;line-height:20px;color:var(--green);margin-left:33px}
.feature p{text-indent:33px;margin-top:-2px}

.about{top:770px;width:360px}
.section-title{font-family:"Yanone Kaffeesatz",sans-serif;font-weight:400;font-size:17px;line-height:22px;color:var(--green)}
.about p{margin-bottom:12px}
.about .btn{margin-top:1px}

.contact{top:770px;left:514px;width:340px}
.contact label{display:block;font-size:10px;line-height:15px;color:var(--text)}
.contact .field{display:block;width:273px;height:26px;border:1px solid var(--input-border);background:var(--page);margin-bottom:9px}
.contact .message{width:329px;height:120px}
.contact .btn{margin-top:10px;margin-left:2px}

.site-footer{position:absolute;left:0;top:1160px;width:1005px;height:40px;background:var(--footer)}
.site-footer p{position:absolute;left:137px;top:12px;color:#eeeeee;font-size:8.5px}
</style>
</head>
<body>

<header class="wrap site-header">
  <div class="brand">
    <span class="brand-mark"></span>
    <span class="brand-name">Harbinger<br>Press<br>Collective</span>
  </div>
  <nav class="main-nav">
    <a href="#" class="active">Home</a>
    <a href="#">About</a>
    <a href="#">Who We Are</a>
    <a href="#">Contact</a>
  </nav>
</header>

<section class="wrap hero" role="img" aria-label="Illustration of Willowmere Commons with its memorial arch, trees and strolling visitors under a soft green sky">
  <div class="hero-caption">
    <h1>Images And Words</h1>
    <p>Praesent nec aliquet elit. Nullam convallis placerat metus, sit amet ultrices nulla faucibus sit amet. Quisque dictum lorem sed sem pharetra luctus.</p>
  </div>
  <span class="slider-btn prev"><svg width="12" height="12" viewBox="0 0 12 12"><path d="M8 2 L4 6 L8 10" fill="none" stroke="#fff" stroke-width="2.2"/></svg></span>
  <span class="slider-btn next"><svg width="12" height="12" viewBox="0 0 12 12"><path d="M4 2 L8 6 L4 10" fill="none" stroke="#fff" stroke-width="2.2"/></svg></span>
</section>

<div class="wrap band" style="top:447px"></div>

<section class="wrap welcome">
  <h2>Welcome to <span>Harbinger Marketing</span></h2>
  <p>Lorem ipsum dolor sit amet, consectetur adipiscing elit. Duis nec purus tellus, quis pulvinar tortor. Sed mattis lobortis gravida. Integer convallis ipsum in neque tempus posuere.</p>
</section>

<div class="wrap band" style="top:547px"></div>

<section class="wrap features">
  <div class="intro">
    <h2>WHO WE ARE</h2>
    <p>Lorem ipsum dolor sit amet, consec adipiscing elit. Duis nec purus.</p>
    <a href="#" class="btn">Read More</a>
  </div>
  <div class="feature" style="left:189px">
    <span class="num">1</span>
    <h3>Business Consulting</h3>
    <p>Lorem ipsum dolor sit amet, consecadipiscing elit. Duis nec purus tellus, quis pulvinar tortor. Sed mattis loborti gravida. Integer convallis.</p>
  </div>
  <div class="feature" style="left:377px">
    <span class="num">2</span>
    <h3>Strategic Planning</h3>
    <p>Lorem ipsum dolor sit amet, consecadipiscing elit. Duis nec purus tellus, quis pulvinar tortor. Sed mattis loborti gravida. Integer convallis.</p>
  </div>
  <div class="feature" style="left:566px">
    <span class="num">3</span>
    <h3>Objective Listening</h3>
    <p>Lorem ipsum dolor sit amet, consecadipiscing elit. Duis nec purus tellus, quis pulvinar tortor. Sed mattis loborti gravida. Integer convallis.</p>
  </div>
</section>

<div class="wrap band" style="top:730px"></div>

<section class="wrap about">
  <h2 class="section-title">About Us</h2>
  <p>Fusce scelerisque pellentesque mi. Suspendisse elementum tellus ut quam pharetra vel volutpat et, euismod eu sem. Aliquam eget lacus magna quis.</p>
  <p>Fusce scelerisque pellentesque mi. Suspendisse elementum tellus ut quam pharetra vel volutpat et, euismod eu sem. Aliquam eget lacus magna quis.</p>
  <p>Fusce scelerisque pellentesque mi. Suspendisse elementum tellus ut quam pharetra vel volutpat et, euismod eu sem. Aliquam eget lacus magna quis.</p>
  <p>Fusce scelerisque pellentesque mi. Suspendisse elementum tellus ut quam pharetra vel volutpat et, euismod eu sem. Aliquam eget lacus magna quis.</p>
  <p>Fusce scelerisque pellentesque mi. Suspendisse elementum tellus ut quam pharetra vel volutpat et, euismod eu sem. Aliquam eget lacus magna quis.</p>
  <p>Lorem ipsum dolor sit amet, consec adipiscing elit. Duis nec purus mattis lobortis gravida. Aliquam eget lacus magna, quis posuere tellus. Fusce scelerisque pellentesque mi. Suspendisse elementum tellus ut quam pharetra vel volutpat et, euismod eu sem.</p>
  <a href="#" class="btn">Continue Reading</a>
</section>

<section class="wrap contact">
  <h2 class="section-title">Contact Us</h2>
  <label for="name">Name:</label>
  <input id="name" class="field" type="text">
  <label for="email">E-mail:</label>
  <input id="email" class="field" type="text">
  <label for="subject">Subject:</label>
  <input id="subject" class="field" type="text">
  <label for="message">Message:</label>
  <textarea id="message" class="field message"></textarea>
  <a href="#" class="btn">Send Message</a>
</section>

<footer class="site-footer">
  <p>Copyright © 2014 Harbinger Marketing. All rights reserved</p>
</footer>

</body>
</html>
```